Belford & Company

We are a boutique commercial real estate firm. For our Business card design - sleek, modern, yet high-end/classy. Please see our website: belfordandcompany.example for details.

We currently need 2 business card names and the ability to add/change the business card information -
Name, Title, Address, Office #, Mobile #, Fax, Email and company website.

Industry/Entity Type

Real Estate

Contact Information for Business Card

Business card design - sleek, modern, yet high-end/classy. Please see our website: belfordandcompany.example for details.

Also, we'd like to have our slogan "Careful Work Builds Lasting Value." somewhere in there. We'd like to make some part of it raised or a different texture if possible.
Color #'s:
blue 19 36 128
light gray 222 222 221
dark gray 107 120 128

Also, we'd like to have our slogan "Careful Work Builds Lasting Value." somewhere in there. We'd like to make some part of it raised or a different texture if possible - grey on one side and blue on the other - rounded edges preferred. Maybe either metal/silver/grey raised logo on the back. Thank you!!

Requirements
Must have
• Sleek, modern, clean and classy design

```html
<!DOCTYPE html>
<html lang="en">
<head>
<meta charset="utf-8">
<title>Belford &amp; Company – Business Card</title>
<link rel="stylesheet" href="https://fonts.googleapis.com/css2?family=Bebas+Neue&family=Lato:wght@400;700&display=swap">
<style>
  :root {
    --blue: #213f9c;
    --blue-deep: #132480;
    --slate: #778a96;
    --light-gray: #dedddd;
    --silver: #c7cacf;
    --white: #ffffff;
    --stage: #e3e3e3;
  }
  * { box-sizing: border-box; margin: 0; padding: 0; }
  html, body { width: 1200px; height: 895px; overflow: hidden; }
  body {
    background: var(--stage);
    font-family: "Lato", sans-serif;
    position: relative;
  }
  .card {
    position: absolute;
    width: 540px;
    height: 310px;
    border-radius: 18px;
    overflow: hidden;
    top: 292px;
  }

  /* Front */
  .card-front { left: 40px; background: var(--blue); }
  .brand {
    position: absolute;
    left: 0; right: 0; top: 92px;
    display: flex; flex-direction: column; align-items: center;
  }
  .brand-row { display: flex; align-items: center; gap: 16px; }
  .brand-square { width: 34px; height: 34px; background: var(--silver); }
  .brand-name {
    font-family: "Bebas Neue", sans-serif;
    font-size: 62px; line-height: 1;
    color: var(--silver); letter-spacing: 1px;
    white-space: nowrap;
  }
  .brand-rule { width: 300px; height: 1px; background: var(--silver); margin: 10px 0 8px; }
  .brand-tagline {
    font-size: 14px; letter-spacing: 7px; color: var(--silver);
    text-transform: uppercase;
  }

  /* Back */
  .card-back { left: 620px; background: var(--slate); }
  .back-brand {
    position: absolute; left: 0; right: 0; top: 58px;
    display: flex; justify-content: center; align-items: center; gap: 10px;
  }
  .back-brand-square { width: 16px; height: 16px; background: var(--white); }
  .back-brand-name {
    font-family: "Bebas Neue", sans-serif; font-size: 34px; color: var(--white); line-height: 1;
    white-space: nowrap;
  }
  .divider {
    position: absolute; left: 26px; right: 26px; top: 172px;
    height: 1px; background: var(--blue-deep);
  }
  .person { position: absolute; top: 118px; }
  .person-left { left: 26px; }
  .person-right { right: 26px; text-align: right; }
  .person-name {
    font-family: "Bebas Neue", sans-serif; font-size: 30px; line-height: 1;
    color: var(--blue);
  }
  .person-title { font-size: 13px; color: var(--white); margin-top: 2px; }

  .contacts {
    position: absolute; left: 26px; top: 184px;
    list-style: none; font-size: 12.5px; color: var(--white); line-height: 17px;
  }
  .contacts li { display: flex; align-items: center; gap: 8px; }
  .contacts svg { width: 11px; height: 11px; flex: none; }
  .contacts .link { color: var(--blue-deep); }

  .address {
    position: absolute; right: 26px; top: 196px;
    text-align: right; font-size: 12.5px; line-height: 16px; color: var(--white);
  }
  .raised-strip {
    position: absolute; left: 0; bottom: 0; width: 332px; height: 16px;
    background: var(--light-gray);
  }
  .slogan-tab {
    position: absolute; right: 0; bottom: 0; width: 224px; height: 34px;
    background: var(--blue);
    clip-path: polygon(14px 0, 100% 0, 100% 100%, 0 100%);
    display: flex; align-items: center; justify-content: center;
    color: var(--white); font-size: 13px; padding: 0 10px 0 20px;
    white-space: nowrap;
  }
</style>
</head>
<body>

<section class="card card-front" aria-label="Card front">
  <div class="brand">
    <div class="brand-row">
      <span class="brand-square"></span>
      <span class="brand-name">Belford &amp; Company</span>
    </div>
    <div class="brand-rule"></div>
    <div class="brand-tagline">Realty Advisors</div>
  </div>
</section>

<section class="card card-back" aria-label="Card back">
  <div class="back-brand">
    <span class="back-brand-square"></span>
    <span class="back-brand-name">Belford &amp; Company</span>
  </div>

  <div class="person person-left">
    <div class="person-name">Daniel Hart</div>
    <div class="person-title">Director Construction</div>
  </div>
  <div class="person person-right">
    <div class="person-name">Mark Ellis</div>
    <div class="person-title">Director Finance</div>
  </div>
  <div class="divider"></div>

  <ul class="contacts">
    <li><svg viewBox="0 0 12 12" fill="none" stroke="#132480" stroke-width="1.4"><rect x="3" y="1" width="6" height="10" rx="1"/></svg>000 000 0000</li>
    <li><svg viewBox="0 0 12 12" fill="#132480"><path d="M1 4 Q6 0 11 4 L9 6 L8 4.5 H4 L3 6 Z"/><rect x="2.5" y="6.5" width="7" height="4.5" rx="1"/></svg>000 000 0000</li>
    <li><svg viewBox="0 0 12 12" fill="#132480"><rect x="3" y="1" width="6" height="3"/><rect x="1" y="4.5" width="10" height="5" rx="1"/><rect x="3" y="8" width="6" height="3"/></svg>000 000 0000</li>
    <li><svg viewBox="0 0 12 12" fill="none" stroke="#132480" stroke-width="1.3"><rect x="1" y="2.5" width="10" height="7"/><path d="M1 2.5 L6 7 L11 2.5"/></svg><span>info@<span class="link">belfordandcompany.example</span></span></li>
    <li><svg viewBox="0 0 12 12" fill="none" stroke="#132480" stroke-width="1.4"><circle cx="7" cy="5" r="3.5"/><path d="M4.5 7.5 L1 11"/></svg><span>www.<span class="link">belfordandcompany.example</span></span></li>
  </ul>

  <div class="address">Box 40512, Riverton<br>Ashford 7021<br>NZ</div>

  <div class="raised-strip"></div>
  <div class="slogan-tab">Careful Work Builds Lasting Value</div>
</section>

</body>
</html>
```